Plakat-Design für Pfandhaus gesucht
Zielgruppe
Wir sind ein Pfandhaus wir vergeben Pfandkredite gegen Wertgegenstände sowie Juwelier und Goldankauf aber in erster Linie steht das Pfandhaus .
Aufgabenstellung
Ich möchte gerne Plakate Buchen die an Straßen oder Hauswänden befestigt sind. Ca.3,5x3 Meter. Die Botschaft muss kurz und knapp sein da die Leute ja vorbeifahren.

```html
<!DOCTYPE html>
<html lang="de">
<head>
<meta charset="utf-8">
<title>Sofort Bargeld – Martin Velden Pfandkredit</title>
<link rel="stylesheet" href="https://fonts.googleapis.com/css2?family=Open+Sans:wght@800&family=PT+Sans:wght@400;700&display=swap">
<style>
  :root {
    --slate: #4a4a4a;
    --white: #ffffff;
    --gold-deep: #cbaa47;
    --gold-mid: #e2bc4c;
    --gold-light: #f8cf56;
    --gold-line: #c9a94a;
  }
  html, body {
    margin: 0;
    padding: 0;
    overflow: hidden;
    background: var(--slate);
  }
  .poster {
    display: block;
    width: 1200px;
    height: 1029px;
    background: var(--slate);
  }
  .headline {
    font-family: "Open Sans", sans-serif;
    font-weight: 800;
    fill: var(--white);
    filter: drop-shadow(3px 4px 3px rgba(0,0,0,0.45));
  }
  .claim {
    font-family: "PT Sans", sans-serif;
    font-weight: 700;
    fill: var(--slate);
  }
  .tick {
    fill: none;
    stroke: var(--white);
    stroke-width: 3.5;
    stroke-linecap: round;
    stroke-linejoin: round;
  }
  .address {
    font-family: "PT Sans", sans-serif;
    font-weight: 700;
    fill: var(--white);
    font-size: 44px;
  }
  .contact {
    font-family: "PT Sans", sans-serif;
    font-weight: 400;
    fill: var(--white);
    font-size: 33px;
  }
  .brand-frame {
    fill: none;
    stroke: var(--gold-line);
  }
  .brand-name {
    font-family: "PT Sans", sans-serif;
    font-weight: 700;
    fill: var(--gold-line);
  }
</style>
</head>
<body>
<svg class="poster" viewBox="0 0 1200 1029" xmlns="http://www.w3.org/2000/svg">
  <defs>
    <linearGradient id="goldBand" x1="0" y1="0" x2="1" y2="0">
      <stop offset="0" stop-color="var(--gold-mid)"/>
      <stop offset="0.35" stop-color="var(--gold-deep)"/>
      <stop offset="1" stop-color="var(--gold-light)"/>
    </linearGradient>
  </defs>

  <!-- top accent stripe -->
  <polygon points="0,68 996,0 1020,0 0,87" fill="url(#goldBand)"/>

  <!-- gold band -->
  <polygon points="0,523 1200,418 1200,557 0,660" fill="url(#goldBand)"/>

  <!-- headline -->
  <g transform="rotate(-5 185 223)">
    <text class="headline" x="185" y="223" font-size="162" textLength="585" lengthAdjust="spacingAndGlyphs">SOFORT</text>
  </g>
  <g transform="rotate(-5 52 472)">
    <text class="headline" x="52" y="472" font-size="285" textLength="1102" lengthAdjust="spacingAndGlyphs">BARGELD</text>
  </g>

  <!-- band claim -->
  <g transform="rotate(-5 43 611)">
    <text class="claim" x="43" y="611" font-size="82" letter-spacing="6">GEGEN PFAND!</text>
  </g>

  <g transform="rotate(-5 637 515)">
    <path class="tick" d="M637 503 l7 9 l16 -20"/>
    <text class="claim" x="689" y="515" font-size="42">Technik</text>
    <path class="tick" d="M853 503 l7 9 l16 -20"/>
    <text class="claim" x="898" y="515" font-size="42">Gold</text>
    <path class="tick" d="M1005 503 l7 9 l16 -20"/>
    <text class="claim" x="1055" y="515" font-size="42">Silber</text>
    <path class="tick" d="M637 553 l7 9 l16 -20"/>
    <text class="claim" x="689" y="565" font-size="42">Hochwertiges Werkzeug</text>
  </g>

  <!-- address block -->
  <text class="address" x="434" y="764" text-anchor="end">Lindenallee 12</text>
  <text class="address" x="434" y="817" text-anchor="end">66113 Saarbrücken</text>
  <text class="contact" x="434" y="896" text-anchor="end">0681 - 55 120 480</text>
  <text class="contact" x="434" y="936" text-anchor="end">www.pfandkredit-velden.de</text>

  <!-- brand panel -->
  <rect class="brand-frame" x="482" y="662" width="664" height="324" stroke-width="3"/>
  <rect class="brand-frame" x="488" y="668" width="652" height="312" stroke-width="1.2"/>
  <text class="brand-name" x="814" y="818" text-anchor="middle" font-size="64">Martin Velden</text>
  <text class="brand-name" x="814" y="884" text-anchor="middle" font-size="48">Pfandkredit</text>
</svg>
</body>
</html>
```